TARO PTY LTD - Business Cards

Design a modern business card - using the attached Designs.
Same design as on the front, apart from the names/numbers/emails to be different.
We want the cards to be very glossy to stand out, do I think the simple black/white/metallic will be effective.
Both lots of details below:

Lyle Marrick
Director
lyle_taro@quintmail.example
0493 628 304

Simon Prowle
Director
simon_taro@quintmail.example
0438 514 209

```html
<!DOCTYPE html>
<html lang="en">
<head>
<meta charset="utf-8">
<title>TARO PTY LTD – Business Cards</title>
<link rel="stylesheet" href="https://fonts.googleapis.com/css2?family=Lato:wght@400;700&display=swap">
<style>
  :root {
    --backdrop: #2c2c2e;
    --card-black: #050505;
    --ink-white: #f4f4f4;
    --ink-soft: #d6d6d6;
    --swoosh-slate: #3a3f45;
    --swoosh-edge: #9aa1a8;
    --mark-silver: #c9cdd1;
  }
  * { box-sizing: border-box; margin: 0; padding: 0; }
  html, body {
    width: 1200px;
    height: 926px;
    overflow: hidden;
    background: var(--backdrop);
    font-family: "Lato", Arial, sans-serif;
  }
  .card-sheet {
    width: 1200px;
    height: 926px;
    display: flex;
    flex-direction: column;
    align-items: center;
    justify-content: center;
    gap: 40px;
  }
  .business-card {
    position: relative;
    width: 700px;
    height: 400px;
    background: var(--card-black);
    overflow: hidden;
    color: var(--ink-white);
  }
  .swoosh {
    position: absolute;
    inset: 0;
    width: 100%;
    height: 100%;
  }
  .contact-block {
    position: absolute;
    top: 78px;
    left: 170px;
    width: 420px;
  }
  .name-row {
    display: flex;
    align-items: flex-end;
    gap: 4px;
  }
  .role {
    font-size: 15px;
    letter-spacing: 3px;
    padding-bottom: 3px;
    border-bottom: 1.5px solid var(--ink-white);
    margin-bottom: 4px;
    line-height: 1;
  }
  .person-name {
    font-size: 30px;
    font-weight: 700;
    letter-spacing: 3px;
    text-transform: uppercase;
    line-height: 1;
  }
  .details {
    margin-top: 16px;
    padding-left: 30px;
    font-size: 16px;
    letter-spacing: 1.5px;
    line-height: 1.55;
    color: var(--ink-soft);
  }
  .details .label {
    font-weight: 700;
    color: var(--ink-white);
  }
  .company-mark {
    position: absolute;
    left: 230px;
    top: 232px;
    display: flex;
    align-items: center;
    gap: 10px;
    color: var(--mark-silver);
  }
  .company-mark .dot {
    width: 18px;
    height: 18px;
    border-radius: 50%;
    background: var(--mark-silver);
  }
  .company-mark .company-name {
    font-size: 26px;
    font-weight: 700;
    letter-spacing: 2px;
  }
</style>
</head>
<body>
<main class="card-sheet">

  <article class="business-card">
    <svg class="swoosh" viewBox="0 0 700 400" aria-hidden="true">
      <path d="M0 292 Q 230 250 700 400 L 0 400 Z" fill="var(--swoosh-edge)"/>
      <path d="M0 299 Q 230 258 700 404 L 0 404 Z" fill="var(--swoosh-slate)"/>
    </svg>
    <div class="contact-block">
      <div class="name-row">
        <span class="role">DIRECTOR</span>
        <span class="person-name">Lyle Marrick</span>
      </div>
      <div class="details">
        <p><span class="label">PHONE:</span> 0493 628 304</p>
        <p><span class="label">EMAIL:</span> lyle_taro@quintmail.example</p>
      </div>
    </div>
    <div class="company-mark">
      <span class="dot"></span>
      <span class="company-name">TARO PTY LTD</span>
    </div>
  </article>

  <article class="business-card">
    <svg class="swoosh" viewBox="0 0 700 400" aria-hidden="true">
      <path d="M0 292 Q 230 250 700 400 L 0 400 Z" fill="var(--swoosh-edge)"/>
      <path d="M0 299 Q 230 258 700 404 L 0 404 Z" fill="var(--swoosh-slate)"/>
    </svg>
    <div class="contact-block">
      <div class="name-row">
        <span class="role">DIRECTOR</span>
        <span class="person-name">Simon Prowle</span>
      </div>
      <div class="details">
        <p><span class="label">PHONE:</span> 0438 514 209</p>
        <p><span class="label">EMAIL:</span> simon_taro@quintmail.example</p>
      </div>
    </div>
    <div class="company-mark">
      <span class="dot"></span>
      <span class="company-name">TARO PTY LTD</span>
    </div>
  </article>

</main>
</body>
</html>
```